Postcard Design

I am an attorney in Pittsburgh. Here and across country, companies are sending data with names, address and new criminal charges for people. This has resulted in some people getting 12 or more of these letters. I want to do a postcard because one does not need to open a postcard. I also want to be delicate since there is no sealed envelope. I want to throw in other matters other than criminal so it does not look like the person is necessarily charged with a crime.
At top would be "Law Office of Dorian F. Haslbeck"
Then:
Need an Attorney?
Attorney Dorian F. Haslbeck has 25 Years of Experience
Free Consultation - Affordable Fees - Credit Cards Accepted
-All Criminal Matters
-Most Civil Matters
-DUI / Traffic Citations / License Restoration
412-555-0187
www.lakesidedefenselawyer.example
www.dfhcounsel.example

My CTQ ranking is A+ but I am not sure they give a logo with the rating. I have all my logos at www.lakesidedefenselawyer.example The purpose of the two websites is these are postcards. I want no one to think oh this person is charged with a crime.

Industry/Entity Type

Attorney

```html
<!DOCTYPE html>
<html lang="en">
<head>
<meta charset="utf-8">
<title>Law Office of Dorian F. Haslbeck – Postcard</title>
<link rel="stylesheet" href="https://fonts.googleapis.com/css2?family=Cinzel:wght@400;500&family=Raleway:ital,wght@0,300;0,400;1,400&display=swap">
<style>
  :root{
    --maroon-deep:#1e0a10;
    --maroon:#3c1220;
    --maroon-ink:#6a1f36;
    --band-dark:rgba(18,14,22,.72);
    --paper:#e4e3e3;
    --paper-edge:#cfcfcf;
    --bar-gray:#6d6d6f;
    --white:#ffffff;
    --soft-white:#ecebef;
    --badge-blue:#1d5fa6;
    --badge-gold:#c9a23c;
    --badge-navy:#1c2d5c;
    --badge-brown:#4a2a2c;
  }
  html,body{margin:0;padding:0;overflow:hidden;background:var(--maroon-deep);}
  .postcard{
    position:relative;width:927px;height:1200px;overflow:hidden;
    background:radial-gradient(ellipse at 50% 0%, #5a1a2c 0%, var(--maroon) 40%, var(--maroon-deep) 100%);
    font-family:"Cinzel",serif;color:var(--white);
  }
  .headline{
    position:absolute;top:58px;left:0;width:927px;margin:0;text-align:center;
    font-weight:400;font-size:76px;letter-spacing:-1px;line-height:1;
    color:var(--soft-white);text-shadow:0 3px 6px rgba(0,0,0,.6);
  }
  .courtroom-photo{
    position:absolute;top:184px;left:0;width:927px;height:612px;
    background:
      linear-gradient(180deg, rgba(60,18,32,.9) 0%, rgba(60,18,32,0) 18%),
      linear-gradient(90deg, #3a3f5c 0%, #5a3d48 22%, #6b2c22 55%, #5b2a22 78%, #4c4e66 100%);
  }
  .courtroom-photo::after{
    content:"";position:absolute;left:0;right:0;bottom:0;height:46%;
    background:linear-gradient(180deg, rgba(80,30,22,0) 0%, #4a1e17 60%, #2a100d 100%);
  }
  .experience-intro{
    position:absolute;top:212px;left:64px;margin:0;
    font-family:"Raleway",sans-serif;font-weight:300;font-size:27px;
    letter-spacing:.2px;color:var(--white);
  }
  .practice-areas{position:absolute;top:250px;left:0;margin:0;padding:0;list-style:none;}
  .practice-areas li{
    height:69px;margin-bottom:2px;background:var(--band-dark);
    font-size:44px;line-height:69px;padding-left:60px;box-sizing:border-box;
    color:var(--white);white-space:nowrap;
  }
  .practice-areas .criminal{width:586px;}
  .practice-areas .civil{width:532px;}
  .practice-areas .traffic{width:624px;}
  .practice-areas .license{width:568px;}
  .contact-strip{
    position:absolute;top:796px;left:0;width:927px;height:36px;
    background:rgba(10,6,8,.85);display:flex;justify-content:center;align-items:center;gap:14px;
    font-size:17px;color:var(--white);font-family:"Cinzel",serif;
  }
  .contact-strip .phone{font-family:"Raleway",sans-serif;font-size:19px;}
  .contact-strip .sep{font-size:8px;opacity:.8;}
  .identity-band{
    position:absolute;top:832px;left:0;width:927px;height:162px;
    background:linear-gradient(180deg,#ececec,var(--paper) 50%,#d9d9d9);
    text-align:center;color:var(--maroon-ink);
  }
  .identity-band .office-label{
    margin:0;padding-top:16px;font-family:"Raleway",sans-serif;font-weight:300;
    font-size:18px;letter-spacing:11px;text-transform:uppercase;
  }
  .identity-band .attorney-name{
    margin:2px 0 0;font-weight:400;font-size:70px;line-height:1;letter-spacing:-1px;
  }
  .identity-band .tagline{
    margin:12px 0 0;font-family:"Raleway",sans-serif;font-style:italic;font-weight:400;
    font-size:16px;letter-spacing:8px;text-transform:uppercase;
  }
  .offer-bar{
    position:absolute;top:996px;left:0;width:927px;height:30px;
    background:var(--bar-gray);border-top:1px solid #8a8a8a;border-bottom:1px solid #4a4a4a;
    display:flex;justify-content:center;align-items:center;gap:16px;
    font-size:21px;color:var(--white);
  }
  .credentials{position:absolute;top:1050px;left:0;width:927px;height:120px;}
</style>
</head>
<body>
<main class="postcard">
  <h1 class="headline">NEED AN ATTORNEY?</h1>

  <div class="courtroom-photo" role="img" aria-label="Photograph of an empty wood-paneled courtroom with judge's bench, flag and gallery benches"></div>

  <p class="experience-intro">25 YEARS OF EXPERIENCE IN</p>
  <ul class="practice-areas">
    <li class="criminal">ALL CRIMINAL MATTERS</li>
    <li class="civil">MOST CIVIL MATTERS</li>
    <li class="traffic">DUI / TRAFFIC CITATIONS</li>
    <li class="license">LICENSE RESTORATION</li>
  </ul>

  <div class="contact-strip">
    <span class="phone">(412) 555-0187</span>
    <span class="sep">&#9654;</span>
    <span>WWW.LAKESIDEDEFENSELAWYER.EXAMPLE</span>
    <span class="sep">&#9654;</span>
    <span>WWW.DFHCOUNSEL.EXAMPLE</span>
  </div>

  <section class="identity-band">
    <p class="office-label">Law Office of</p>
    <h2 class="attorney-name">DORIAN F. HASLBECK</h2>
    <p class="tagline">Pittsburg Criminal Defense Attorney</p>
  </section>

  <div class="offer-bar">
    <span>FREE CONSULTATION</span><span>|</span><span>AFFORDABLE FEES</span><span>|</span><span>CREDIT CARDS ACCEPTED</span>
  </div>

  <svg class="credentials" viewBox="0 0 927 120" aria-label="Professional credential badges">
    <circle cx="260" cy="58" r="52" fill="var(--badge-brown)" stroke="var(--badge-navy)" stroke-width="4"/>
    <circle cx="260" cy="58" r="38" fill="#e9e6e2"/>
    <rect x="366" y="20" width="206" height="76" rx="10" fill="var(--badge-blue)" stroke="#ffffff" stroke-width="3"/>
    <rect x="369" y="23" width="66" height="70" rx="7" fill="#ffffff"/>
    <circle cx="564" cy="92" r="13" fill="#2a8fa8" stroke="#ffffff" stroke-width="2"/>
    <circle cx="672" cy="58" r="50" fill="var(--badge-navy)" stroke="var(--badge-gold)" stroke-width="4"/>
    <circle cx="672" cy="58" r="34" fill="var(--badge-gold)"/>
  </svg>
</main>
</body>
</html>
```